Car rental website design for a UAE car rental company

This project is about creating a new website design for a car rental company located in Dubai (United Arab Emirates), I opened the same project a few months ago but I didn't receive a lot of appealing entries so I closed it but this time I am marking the project as guaranteed to avoid such situation again, if you have already provided a design before then please re-submit again on this project so that it is considered while reviewing all the designs

A few important things:

1- We need a simple non-complex design
2- The final deliverable would be 2 screens (PSD, JPEG ... etc), the first screen is for the home page and the second screen is for an internal page
3- The home page must have a section that end users can use to rent a car online directly from the home page instead of going into some inner pages
4- The current website is very old and not very appealing so avoid creating a similar design (www.quarvin-drive.example)
5- The name is Quarvin but the company rents normal cars (no Limousin cars will be rented) so avoid adding any fancy cars in the images/graphics used in the design, just normal end users cars
6- The expected pages would be: home, About us, Our team, Strategy, Contact us and links to social media pages
7- The attachments include the company's logo and some screens from other car rental companies that provide online rentals/payments

If you have any questions please feel free to ask and please note that we will need the designs urgently

Thanks

Target Market(s)

Dubai - United Arab Emirates

Industry/Entity Type

It Company

Number of Pages Required

2 page

Font styles to use
Sans Serif

Requirements
Must have
• Check the project details
Nice to have
Should not have

```html
<!DOCTYPE html>
<html lang="en">
<head>
<meta charset="utf-8">
<title>Quarvin Rent A Car</title>
<link href="https://fonts.googleapis.com/css2?family=Roboto+Slab:wght@300;400&family=Open+Sans:wght@400;600&display=swap" rel="stylesheet">
<style>
:root{
  --maroon:#a3053c;
  --grey:#7d7d7d;
  --grey-dark:#333;
  --ring:#8a8a8a;
  --band:#f4f4f4;
  --hero:#d8d8da;
  --line:#c9c9c9;
  --white:#fff;
}
*{box-sizing:border-box;margin:0;padding:0}
html,body{width:1121px;height:1200px;overflow:hidden;background:var(--white)}
body{font-family:"Roboto Slab",Georgia,serif;font-weight:300;color:var(--grey-dark);position:relative}
a{color:inherit;text-decoration:none}

/* header */
.site-header{position:relative;height:98px;border-top:2px solid #bbb;border-bottom:2px solid var(--maroon);background:#fafafa}
.brand{position:absolute;left:74px;top:12px;display:flex;align-items:center;gap:12px}
.brand-mark{width:60px;height:60px;background:var(--maroon)}
.brand-name{font-size:36px;font-weight:400;color:var(--grey)}
.social{display:flex;gap:8px}
.social span{width:23px;height:23px;border-radius:50%;background:#2a5aa8;display:block}
.social span:nth-child(2){background:#3b8fd0}
.social span:nth-child(3){background:#1d6fb0}
.social span:nth-child(4){background:#c9382c}
.site-header .social{position:absolute;left:564px;top:16px}
.call{position:absolute;left:790px;top:10px;display:flex;align-items:center;gap:8px;color:var(--maroon);font-size:18px;font-weight:400}
.main-nav{position:absolute;right:78px;top:66px;display:flex;gap:24px;font-size:16px;color:var(--grey)}
.main-nav a.current{color:var(--maroon)}

/* hero */
.hero{position:relative;height:410px;background:linear-gradient(180deg,#dcdcde,#cfcfd2);border-bottom:3px solid var(--maroon)}
.hero-title{position:absolute;left:86px;top:20px;font-size:31px;font-weight:400;color:var(--maroon);line-height:36px}
.hero-photo{position:absolute;left:165px;top:112px;width:380px;height:295px;border-radius:40px 40px 10px 10px;background:radial-gradient(ellipse at 50% 45%,#b9b9bb,#8f8f92 60%,#cfcfd2 100%)}
.arrow{position:absolute;top:190px;width:36px;height:36px;border-radius:50%;background:#6b6b6b;display:flex;align-items:center;justify-content:center}
.arrow.prev{left:22px}.arrow.next{left:1063px}
.dots{position:absolute;left:96px;top:388px;display:flex;gap:8px}
.dots span{width:16px;height:16px;background:#fff}
.dots span.on{background:var(--maroon)}

/* booking */
.booking{position:absolute;left:654px;top:0;width:394px;height:421px;border:5px solid var(--maroon);border-top:none;background:var(--white)}
.booking-tabs{display:flex;height:40px;background:var(--maroon);margin:0 -5px;padding:6px 5px 0}
.booking-tabs span{font-size:15px;color:#fff;font-weight:400;padding:8px 10px}
.booking-tabs span.active{background:#8e9a91}
.booking-body{position:relative;padding:10px 0 0 0;font-size:14px;font-weight:400}
.step{position:absolute;left:4px;width:24px;height:24px;border:1px solid var(--maroon);display:flex;align-items:center;justify-content:center;font-size:14px}
.field-label{position:absolute;left:45px}
.link{position:absolute;left:45px;color:var(--maroon);text-decoration:underline}
.input{position:absolute;height:26px;border:1px solid #777;font-size:12px;padding:5px 6px;background:#fff}
.spin{position:absolute;right:0;top:0;width:18px;height:24px;border-left:1px solid #777;font-size:9px;text-align:center;line-height:11px}
.check{position:absolute;display:flex;align-items:center;gap:5px;font-size:13.5px}
.check i{width:9px;height:9px;border:1px solid #555;display:block}
.help{width:20px;height:20px;border-radius:50%;background:#8e9a91;color:#fff;font-size:11px;display:inline-flex;align-items:center;justify-content:center;font-style:normal}
.quote-btn{position:absolute;left:254px;top:334px;width:128px;height:40px;background:var(--maroon);color:#fff;font-size:16px;display:flex;align-items:center;justify-content:center}

/* features */
.features{position:relative;height:262px;background:var(--band);border-bottom:1px solid #e2e2e2}
.feature{position:absolute;top:30px;width:250px;text-align:center}
.feature-icon{width:90px;height:90px;border-radius:50%;border:2px solid var(--ring);margin:0 auto 20px;display:flex;align-items:center;justify-content:center;background:#fff}
.feature-icon.hot{border-color:var(--maroon)}
.feature h3{font-size:15px;font-weight:400;line-height:20px;color:#444}
.feature p{font-family:"Open Sans",Arial,sans-serif;font-size:14px;line-height:19px;color:#555;margin-top:7px}
.pager{position:absolute;top:108px;width:26px;height:40px;background:#c4c4c4;display:flex;align-items:center;justify-content:center}
.pager.left{left:32px}.pager.right{left:1063px}

/* text sections */
.intro{text-align:center;padding:0 100px}
.section-title{display:inline-block;font-size:18px;color:var(--grey);border-bottom:1px dashed #999;padding:0 82px 2px;margin-bottom:10px}
.section-title em{font-style:normal;color:var(--maroon);font-weight:400}
.intro p{font-size:13.5px;line-height:21px;font-weight:400;color:#333}
.welcome{padding-top:28px;height:196px}
.read-more{display:block;margin-top:6px;font-size:14.5px;font-weight:400}
.divider{height:1px;margin:8px 80px 0;background:linear-gradient(90deg,transparent,#ccc,transparent)}
.mission{padding-top:28px;height:150px}
.mission p+p{margin-top:4px}

/* footer */
.site-footer{position:absolute;left:0;top:1146px;width:1121px;height:54px;background:var(--maroon);color:#fff;display:flex;align-items:center}
.foot-nav{margin-left:76px;display:flex;gap:18px;font-size:14px;font-weight:400}
.site-footer .social{margin-left:140px}
.site-footer .social span{border:2px solid #fff}
.copy{margin-left:auto;margin-right:22px;font-family:"Open Sans",Arial,sans-serif;font-weight:600;font-size:13px}
</style>
</head>
<body>

<header class="site-header">
  <a class="brand" href="#"><span class="brand-mark"></span><span class="brand-name">Quarvin</span></a>
  <div class="social" aria-label="Social links"><span></span><span></span><span></span><span></span></div>
  <div class="call">
    <svg width="36" height="40" viewBox="0 0 36 40" fill="none" stroke="#555" stroke-width="3"><path d="M5 22V17a13 13 0 0 1 26 0v5"/><rect x="3" y="20" width="7" height="12" rx="2" fill="var(--maroon)" stroke="none"/><rect x="26" y="20" width="7" height="12" rx="2" fill="var(--maroon)" stroke="none"/><path d="M29 32q0 5-9 5"/></svg>
    Call us at +971 4 555 0182
  </div>
  <nav class="main-nav">
    <a class="current" href="#">HOME</a><a href="#">ABOUT US</a><a href="#">OUR TEAM</a><a href="#">STRATEGY</a><a href="#">CONTACT US</a>
  </nav>
</header>

<section class="hero">
  <h1 class="hero-title">Experience An Extra Mile of comfort,<br>pleasure and leisure From the best</h1>
  <div class="hero-photo" role="img" aria-label="Front view photograph of a silver saloon car"></div>
  <a class="arrow prev" href="#"><svg width="14" height="20"><path d="M11 2 3 10l8 8" stroke="#ddd" stroke-width="2" fill="none"/></svg></a>
  <a class="arrow next" href="#"><svg width="14" height="20"><path d="M3 2l8 8-8 8" stroke="#ddd" stroke-width="2" fill="none"/></svg></a>
  <div class="dots"><span></span><span class="on"></span><span></span><span></span></div>

  <form class="booking">
    <div class="booking-tabs"><span class="active">Book A Car</span><span>View / Modify / Cancel A Reservation</span></div>
    <div class="booking-body">
      <span class="step" style="top:12px">1</span>
      <span class="field-label" style="top:12px">Pick-up Location &nbsp;(City, State or Airport Code</span>
      <a class="link" style="top:34px" href="#">Previous Searches</a>
      <div class="input" style="left:45px;top:58px;width:325px">Dubai Airport - Terminal 3</div>
      <a class="link" style="top:90px" href="#">Help me find a rental location</a>
      <label class="check" style="left:45px;top:114px"><i></i>Return car to a different Norvel Location &nbsp;<em class="help">?</em></label>
      <span class="step" style="top:149px">2</span>
      <span class="field-label" style="top:149px">Pick-up Date &amp; Time</span>
      <div class="input" style="left:45px;top:173px;width:160px">26/03/2015</div>
      <div class="input" style="left:210px;top:173px;width:160px">16:00<span class="spin">^<br>v</span></div>
      <span class="field-label" style="top:210px">Return Date &amp; Time</span>
      <div class="input" style="left:45px;top:234px;width:160px">26/03/2015</div>
      <div class="input" style="left:210px;top:234px;width:160px">16:00<span class="spin">^<br>v</span></div>
      <span class="field-label" style="top:271px">Hire Car Type</span>
      <div class="input" style="left:45px;top:295px;width:160px">Automatic</div>
      <label class="check" style="left:213px;top:295px"><i></i>Apply a discount Code<em class="help">?</em></label>
      <a class="quote-btn" href="#">Get A Quote</a>
    </div>
  </form>
</section>

<section class="features">
  <a class="pager left" href="#"><svg width="12" height="20"><path d="M10 2 2 10l8 8" stroke="#fff" stroke-width="2" fill="none"/></svg></a>
  <a class="pager right" href="#"><svg width="12" height="20"><path d="M2 2l8 8-8 8" stroke="#fff" stroke-width="2" fill="none"/></svg></a>

  <div class="feature" style="left:63px">
    <div class="feature-icon hot"><svg width="60" height="44" viewBox="0 0 60 44" fill="var(--maroon)"><path d="M4 20l5-12h22l5 12v10H4z"/><circle cx="11" cy="31" r="4"/><circle cx="29" cy="31" r="4"/><path d="M24 30l5-10h22l5 10v10H24z" stroke="#fff" stroke-width="2"/><circle cx="31" cy="41" r="3"/><circle cx="49" cy="41" r="3"/></svg></div>
    <h3>Wide Range Of Vehicles For City<br>Driving or SUV’s For Trips</h3>
    <p>Lorem ipsum dolor sit<br>aonsectetuer adipiscing elied<br>diam nonummy</p>
  </div>
  <div class="feature" style="left:327px">
    <div class="feature-icon"><svg width="40" height="44" viewBox="0 0 40 44"><path d="M14 8h12l8 12-14 20L6 20z" fill="#8a8a8a" transform="rotate(-30 20 22)"/><circle cx="17" cy="10" r="3" fill="#fff"/><text x="13" y="30" font-size="10" fill="#fff" font-family="Open Sans,sans-serif">%</text></svg></div>
    <h3>Special 10% Discount For New<br>Customers On The First Rent</h3>
    <p>Lorem ipsum dolor sit<br>aonsectetuer adipiscing elied<br>diam nonummy</p>
  </div>
  <div class="feature" style="left:577px">
    <div class="feature-icon"><svg width="44" height="44" viewBox="0 0 44 44" fill="#8a8a8a"><circle cx="20" cy="8" r="5"/><rect x="24" y="6" width="14" height="4"/><path d="M6 28l5-10h22l5 10v10H6z"/><circle cx="13" cy="31" r="3" fill="#fff"/><circle cx="31" cy="31" r="3" fill="#fff"/></svg></div>
    <h3>Long Term Car<br>Rentals</h3>
    <p>Lorem ipsum dolor sit<br>aonsectetuer adipiscing elied<br>diam nonummy</p>
  </div>
  <div class="feature" style="left:826px">
    <div class="feature-icon"><svg width="40" height="40" viewBox="0 0 40 40" fill="none" stroke="#777" stroke-width="5"><path d="M10 14h14a10 10 0 0 1 0 20h-4"/><path d="M16 6 8 14l8 8" stroke-linejoin="round"/></svg></div>
    <h3>Buyback Option After<br>Lease Term</h3>
    <p>Lorem ipsum dolor sit<br>aonsectetuer adipiscing elied<br>diam nonummy</p>
  </div>
</section>

<section class="intro welcome">
  <h2 class="section-title">Welcome to Quarvin <em>Rent A Car</em></h2>
  <p>As Dubai is expected to welcome millions of tourists and visitors, car rental industry is believed to escalate more rapidly in the region.<br>Over the past five years, demands for car rentals in Dubai has been augmenting at a healthy pace and is currently registering a growth<br>rate of 20 to 25 percent per year. The swift economic growth and the number. Quarvin was established to bring comfort<br>and pleasure to all its clients. First rate service plus highly maintained and top...</p>
  <a class="read-more" href="#">Read More</a>
</section>
<div class="divider"></div>

<section class="intro mission">
  <h2 class="section-title">Our <em>Mission</em></h2>
  <p>To be one of the leading auto leasing company in the fast growing economy and tourism industry of the emirate of Dubai &amp; play alongside<br>with the major car rental companies in the globe.</p>
  <p>Quarvin vows to deliver comfort, luxury &amp; satisfaction to all our clients by providing them professional, hassle-free and first class service.</p>
</section>

<footer class="site-footer">
  <nav class="foot-nav"><a href="#">HOME</a><a href="#">ABOUT US</a><a href="#">OUR TEAM</a><a href="#">STRATEGY</a><a href="#">CONTACT US</a></nav>
  <div class="social" aria-label="Social links"><span></span><span></span><span></span><span></span></div>
  <p class="copy">© 2015 Quarvin. All Rights Reserved</p>
</footer>

</body>
</html>
```